Harbor - Security & Risk Management Firm needs a flier designed

Our firm needs a one page, front and back flier designed to represent our services. The one side of the flier should highlight our premium guard services, as we only hire prior military and law enforcement personnel. The reverse, should promote our Remote Video Guarding Service. OUr firm is owned and operated by U.S. Military and law enforcement veterans.

Target Market(s)

Commercial and Government Clients

Industry/Entity Type

Security Service

Font styles to use
Sans Serif

Colors

Designer to choose colors to be used in the design.

Requirements
Must have
• SIDE 1: Highlight Professional Guard Services, with highlighted points
• - No Long Term Contracts! Month-to-month terms
• - All armed officers have minimum 5+ years U.S. Military and/or law enforcement experience
• - Officers are trained in Active Shooter Response
• - Professional, Courteous and Dependable
• SIDE 2: Highlight Remote Video Guarding Services
• "OUR KORVEX, REMOTE VIDEO GUARDING SOLUTION, IS TRUSTED BY THOUSANDS OF SATISFIED CUSTOMERS. ANY SUSPICIOUS OR CRIMINAL ACTIVITY IS MET WITH OUR TRAINED AND LICENSED OPERATORS WHO IDENTIFY THE SITUATION, SOUND SIRENS, TURN ON LIGHTS, CONTACT CUSTOMERS AND DISPATCH LAW ENFORCEMENT OR LOCAL SECURITY TEAMS. WE LEAD THE INDUSTRY IN UNMATCHED PROFESSIONALISM, EXPERTISE, INDUSTRY LEADING RESOLUTION, ANALYTICS, AND INTRUSION DETECTION.
• EXPERIENCE THE BRAMLOCK DIFFERENCE TODAY, BY CONTACTING OUR TEAM NOW FOR A FREE CONSULTATION."
• Starting as low as $795/month
• DESIGN STYLE: The design should reflect a high end, professional brand. But should also have some of a tactical feel, that represents our foundation of military and law enforcement professionals.
• Colors: Company colors are Navy Blue and Silver/Grey - These are the colors that should be used, to match our logo
• Contact info:
• Web: www.BRAMLOCK.example
• Phone: 1-833-555-0142
• Must include our logo, company name, and contact info on bottom of each side.
• Flier size 8.5"x11"
• Final project should be delivered in Photoshop or Adobe Illustrator
Nice to have
• I like the use of images inside or mixed with shapes such as hexagons.
• Feel free to use our website: www.bramlock.example and use any content or imagery in the design.
• I also like conveying messages with images and icons. Want the overall feel to be clean and simple.
• We are trying to create our brand and the flier should be a good representation of our brand.

```html
<!DOCTYPE html>
<html lang="en">
<head>
<meta charset="utf-8">
<title>Harbor - Security Flier</title>
<link href="https://fonts.googleapis.com/css2?family=Roboto+Condensed:wght@400;700;900&family=Lato:wght@400;700&display=swap" rel="stylesheet">
<style>
  :root{
    --navy:#0f1445;
    --navy-deep:#0a0e33;
    --silver:#8e9196;
    --steel:#4a4d52;
    --paper:#f1f2f4;
    --ink:#1b1d24;
    --stage:#e6e6e6;
    --white:#ffffff;
  }
  *{box-sizing:border-box;margin:0;padding:0}
  html,body{width:1200px;height:1200px;overflow:hidden;background:var(--stage)}
  .canvas{position:relative;width:1200px;height:1200px}
  .page{position:absolute;width:657px;height:850px;transform:scale(.822);transform-origin:top left;overflow:hidden;
    background:linear-gradient(160deg,#f7f8f9 0%,var(--paper) 50%,#e4e6ea 100%);
    box-shadow:0 6px 18px rgba(0,0,0,.25);font-family:"Roboto Condensed",sans-serif;color:var(--ink)}
  .page--front{left:40px;top:250px}
  .page--back{left:620px;top:250px}
  .art{position:absolute;left:0;top:0;width:657px;height:850px}
  .abs{position:absolute}

  .hero-title{left:362px;top:296px;width:295px;text-align:center;line-height:1}
  .hero-title .pre{font-weight:700;font-size:33px;color:var(--white);letter-spacing:.5px}
  .hero-title .main{font-weight:900;font-size:66px;color:var(--navy);margin-top:4px;letter-spacing:1px}
  .hero-title .post{font-weight:700;font-size:42px;color:var(--white);margin-top:2px}

  .brand{display:flex;align-items:center;gap:8px}
  .brand__mark{width:44px;height:44px;background:var(--navy)}
  .brand__name{font-weight:700;font-size:40px;color:var(--navy);line-height:1;letter-spacing:.5px}
  .brand__tag{font-family:"Roboto Condensed",sans-serif;font-size:13px;color:var(--navy);letter-spacing:.6px;margin-top:2px}
  .brand--front{left:34px;top:402px}

  .feature{width:170px;text-align:center;font-weight:700;font-size:12px;line-height:1.3;color:var(--ink);white-space:nowrap}

  .footer-text{display:flex;gap:14px;font-family:"Lato",sans-serif;font-size:10.5px;color:var(--white);align-items:center}
  .footer-text svg{width:10px;height:10px}

  .back-title{left:89px;top:22px;width:480px;text-align:center;color:var(--white);line-height:1}
  .back-title .main{font-weight:900;font-size:48px;letter-spacing:.5px}
  .back-title .sub{font-family:"Lato",sans-serif;font-size:26px;margin-top:4px}

  .site-label{width:140px;text-align:center;font-weight:700;font-size:12px;color:var(--ink)}

  .body-copy{left:26px;top:594px;width:608px;font-family:"Lato",sans-serif;font-size:13.2px;line-height:1.27;text-align:justify;text-align-last:center;color:var(--ink)}

  .cta{left:0;top:688px;width:657px;height:72px;background:var(--navy);color:var(--white);text-align:center}
  .cta .lead{font-family:"Lato",sans-serif;font-size:16px;padding-top:9px}
  .cta .bold{font-weight:700;font-size:27px;margin-top:2px;letter-spacing:.3px}

  .brand--back{left:256px;top:770px}
  .brand--back .brand__mark{width:24px;height:24px}
  .brand--back .brand__name{font-size:22px}
  .brand--back .brand__tag{font-size:7px}

  .social{left:480px;top:802px;display:flex;gap:8px}
  .social span{width:15px;height:15px;background:var(--navy);border-radius:3px}
</style>
</head>
<body>
<div class="canvas">

  <section class="page page--front">
    <svg class="art" viewBox="0 0 657 850" xmlns="http://www.w3.org/2000/svg">
      <defs>
        <linearGradient id="flagTone" x1="0" y1="0" x2="1" y2="1">
          <stop offset="0" stop-color="#3a4a86"/><stop offset=".45" stop-color="#d9a3a6"/><stop offset="1" stop-color="#f4f4f6" stop-opacity="0"/>
        </linearGradient>
        <linearGradient id="guardTone" x1="0" y1="0" x2="1" y2="1">
          <stop offset="0" stop-color="#7f8f74"/><stop offset=".55" stop-color="#3d4a3c"/><stop offset="1" stop-color="#1b2030"/>
        </linearGradient>
        <linearGradient id="silverPlate" x1="0" y1="0" x2="0" y2="1">
          <stop offset="0" stop-color="#9a9ca1"/><stop offset=".5" stop-color="#6e7176"/><stop offset="1" stop-color="#9fa2a6"/>
        </linearGradient>
        <linearGradient id="officerTone" x1="0" y1="0" x2="0" y2="1">
          <stop offset="0" stop-color="#4c4f55"/><stop offset="1" stop-color="#23252a"/>
        </linearGradient>
      </defs>

      <rect role="img" aria-label="Waving American flag" x="0" y="0" width="200" height="380" fill="url(#flagTone)"/>
      <polygon points="126,0 582,0 582,250 362,402 126,292" fill="var(--navy)"/>
      <polygon role="img" aria-label="Security guard in cap and sunglasses speaking into a radio" points="120,0 572,0 572,240 357,390 120,256" fill="url(#guardTone)"/>

      <polygon points="203,278 239,299 239,341 203,362 167,341 167,299" fill="none" stroke="#6b6e73" stroke-width="3"/>

      <polygon points="520,643 657,643 657,850 470,850" fill="var(--navy)"/>
      <polygon points="562,516 598,537 598,579 562,600 526,579 526,537" fill="none" stroke="var(--navy)" stroke-width="3"/>

      <polygon points="509,193 657,278 657,448 509,533 362,448 362,278" fill="url(#silverPlate)"/>
      <polygon points="424,208 459,228 459,268 424,288 389,268 389,228" fill="none" stroke="#ffffff" stroke-width="3"/>

      <g fill="var(--steel)" stroke="#2e3034" stroke-width="2">
        <polygon points="94,496 137,521 137,571 94,596 51,571 51,521"/>
        <polygon points="269,496 312,521 312,571 269,596 226,571 226,521"/>
        <polygon points="94,660 137,685 137,735 94,760 51,735 51,685"/>
        <polygon points="269,660 312,685 312,735 269,760 226,735 226,685"/>
      </g>
      <g fill="none" stroke="#ffffff" stroke-width="2" stroke-linejoin="round" stroke-linecap="round">
        <rect x="80" y="526" width="28" height="36" rx="2"/>
        <line x1="86" y1="536" x2="102" y2="536"/><line x1="86" y1="543" x2="102" y2="543"/><line x1="86" y1="550" x2="98" y2="550"/>
        <line x1="72" y1="560" x2="92" y2="540"/>
        <path d="M258 566 v-10 c-10-4-12-14-8-22 c4-10 18-14 28-8 c8 5 9 14 6 20 l4 8 h-5 v6 h-8 v6"/>
        <circle cx="266" cy="535" r="6"/>
        <path d="M252 718 h8 v-18 h-8 z"/>
        <path d="M260 700 l8-14 c3-5 9-3 8 3 l-2 9 h12 c4 0 6 4 5 7 l-4 12 c-1 2-3 3-5 3 h-22" fill="#ffffff"/>
      </g>
      <g fill="#ffffff">
        <circle cx="88" cy="688" r="5"/>
        <path d="M84 695 h9 l4 14 l-6 0 l2 14 h-6 l-3-12 l-6 12 h-6 l6-16 z"/>
        <rect x="86" y="697" width="38" height="3"/>
      </g>

      <rect role="img" aria-label="Security officer with arms crossed, wearing cap and jacket" x="372" y="553" width="180" height="297" fill="url(#officerTone)"/>

      <polygon points="0,820 282,820 300,850 0,850" fill="var(--navy-deep)"/>
      <polygon points="282,820 360,820 378,850 300,850" fill="#8b8e93"/>
    </svg>

    <div class="abs hero-title">
      <div class="pre">PROFESSIONAL</div>
      <div class="main">GUARD</div>
      <div class="post">SERVICES</div>
    </div>

    <div class="abs brand brand--front">
      <div class="brand__mark"></div>
      <div>
        <div class="brand__name">BRAMLOCK</div>
        <div class="brand__tag">—SECURITY &amp; RISK MANAGEMENT—</div>
      </div>
    </div>

    <div class="abs feature" style="left:9px;top:606px">No Long Term Contracts!<br>Month-to-month terms</div>
    <div class="abs feature" style="left:192px;top:600px">All armed officers have minimum<br>5+ years U.S. Military and/or law<br>enforcement experience</div>
    <div class="abs feature" style="left:9px;top:771px">Officers are trained in Active<br>Shooter Response</div>
    <div class="abs feature" style="left:184px;top:771px">Professional, Courteous<br>and Dependable</div>

    <div class="abs footer-text" style="left:24px;top:827px">
      <span><svg viewBox="0 0 10 10"><path d="M2 1 l2 2 l-1 1.5 c.6 1.3 1.3 2 2.5 2.5 l1.5-1 l2 2 l-1.5 1.5 c-4 0-7-3-7-7z" fill="#fff"/></svg> 1-833-555-0142</span>
      <span><svg viewBox="0 0 10 10"><circle cx="5" cy="5" r="4" fill="none" stroke="#fff"/><line x1="1" y1="5" x2="9" y2="5" stroke="#fff"/></svg> www.BRAMLOCK.example</span>
    </div>
  </section>

  <section class="page page--back">
    <svg class="art" viewBox="0 0 657 850" xmlns="http://www.w3.org/2000/svg">
      <defs>
        <linearGradient id="hubFill" x1="0" y1="0" x2="0" y2="1">
          <stop offset="0" stop-color="#9c9ea2"/><stop offset="1" stop-color="#85888d"/>
        </linearGradient>
      </defs>

      <polygon points="75,0 583,0 583,72 327,182 75,72" fill="#6f7277"/>
      <polygon points="89,0 569,0 569,58 327,168 89,58" fill="var(--navy)"/>

      <g stroke="#555" stroke-width="1.5">
        <line x1="200" y1="275" x2="240" y2="293"/>
        <line x1="400" y1="290" x2="440" y2="270"/>
        <line x1="178" y1="383" x2="225" y2="384"/>
        <line x1="433" y1="383" x2="478" y2="384"/>
        <line x1="207" y1="490" x2="248" y2="470"/>
        <line x1="410" y1="470" x2="450" y2="490"/>
      </g>

      <polygon points="329,268 420,321 420,426 329,478 238,426 238,321" fill="#ffffff" stroke="var(--navy)" stroke-width="2"/>
      <polygon role="img" aria-label="Pole-mounted remote video surveillance unit with two dome cameras" points="329,280 410,327 410,419 329,466 248,419 248,327" fill="url(#hubFill)"/>

      <g stroke="#ffffff" stroke-width="3">
        <polygon role="img" aria-label="Construction site with excavator at night" points="138,186 179,210 179,257 138,280 97,257 97,210" fill="#3c4f78"/>
        <polygon role="img" aria-label="Solar panel energy facility" points="516,186 557,210 557,257 516,280 475,257 475,210" fill="#5b6f8f"/>
        <polygon role="img" aria-label="Stacked shipping containers for equipment storage" points="94,310 135,334 135,381 94,404 53,381 53,334" fill="#8c4a45"/>
        <polygon role="img" aria-label="Car dealership lot with vehicles" points="576,310 617,334 617,381 576,404 535,381 535,334" fill="#7b8fae"/>
        <polygon role="img" aria-label="Large residential estate with fountain" points="136,453 177,477 177,524 136,547 95,524 95,477" fill="#6d7a69"/>
        <polygon role="img" aria-label="Cell tower against blue sky" points="526,453 567,477 567,524 526,547 485,524 485,477" fill="#6f94c2"/>
      </g>
      <g fill="none" stroke="#8e9196" stroke-width="1">
        <polygon points="138,183 182,208 182,259 138,283 94,259 94,208"/>
        <polygon points="516,183 560,208 560,259 516,283 472,259 472,208"/>
        <polygon points="94,307 138,332 138,383 94,407 50,383 50,332"/>
        <polygon points="576,307 620,332 620,383 576,407 532,383 532,332"/>
        <polygon points="136,450 180,475 180,526 136,550 92,526 92,475"/>
        <polygon points="526,450 570,475 570,526 526,550 482,526 482,475"/>
      </g>

      <polygon points="0,822 310,822 330,850 0,850" fill="#3a3c41"/>
      <polygon points="310,822 657,822 657,850 330,850" fill="var(--navy)"/>
    </svg>

    <div class="abs back-title">
      <div class="main">REMOTE VIDEO</div>
      <div class="sub">Guarding Services</div>
    </div>

    <div class="abs site-label" style="left:68px;top:288px">Construction sites</div>
    <div class="abs site-label" style="left:446px;top:293px">Energy Facilities</div>
    <div class="abs site-label" style="left:24px;top:416px">Equipment Storage</div>
    <div class="abs site-label" style="left:506px;top:420px">Auto Dealerships</div>
    <div class="abs site-label" style="left:66px;top:559px">Residential</div>
    <div class="abs site-label" style="left:456px;top:559px">Cell Towers</div>

    <p class="abs body-copy">Our KORVEX, remote video guarding solution, is trusted by thousands of satisfied customers. any suspicious or criminal activity is met with our trained and licensed operators who identify the situation, sound sirens, turn on lights, contact customers and dispatch law enforcement or local security teams. we lead the industry in unmatched professionalism, expertise, industry leading resolution, analytics, and intrusion detection.</p>

    <div class="abs cta">
      <div class="lead">Experience the BRAMLOCK difference today, by contacting</div>
      <div class="bold">OUR TEAM NOW FOR A FREE CONSULTATION</div>
    </div>

    <div class="abs brand brand--back">
      <div class="brand__mark"></div>
      <div>
        <div class="brand__name">BRAMLOCK</div>
        <div class="brand__tag">—SECURITY &amp; RISK MANAGEMENT—</div>
      </div>
    </div>

    <div class="abs social" aria-label="Social media links">
      <span></span><span></span><span></span><span></span><span></span><span></span>
    </div>

    <div class="abs footer-text" style="left:40px;top:829px">
      <span><svg viewBox="0 0 10 10"><path d="M2 1 l2 2 l-1 1.5 c.6 1.3 1.3 2 2.5 2.5 l1.5-1 l2 2 l-1.5 1.5 c-4 0-7-3-7-7z" fill="#fff"/></svg> 1-833-555-0142</span>
      <span><svg viewBox="0 0 10 10"><circle cx="5" cy="5" r="4" fill="none" stroke="#fff"/><line x1="1" y1="5" x2="9" y2="5" stroke="#fff"/></svg> www.BRAMLOCK.example</span>
    </div>
  </section>

</div>
</body>
</html>
```